card design for engineering consultancy

engineering drafting and project management company the provides drafting services for.
Electrical, Hydraulic, Mechanical, and Civil services
The company is called Q7R Services and logo is as attached
Information on card should be.
1. Logo
2.website : Q7RServices.example
3. email : info@Q7RServices.example
4. Phone: (+61) 400512836
5. Motto: Design - Document - Develop - Deliver

this card should be basically used for business identification only

Target Market(s)

electricians plumbers air conditioning installers and civil contractors

Industry/Entity Type

engineering, drafting, electrical, plumbing, airconditioning, civil

Contact Information for Business Card

1. Logo 2.website : Q7RServices.example 3. email : info@Q7RServices.example 4. Phone: (+61) 400512836 5. Motto: Design - Document - Develop - Deliver

Font styles to use
Serif

Requirements
Must have
• logo
Nice to have
• something inovative and different that makes it stand out from being just another business card

```html
<!DOCTYPE html>
<html lang="en">
<head>
<meta charset="utf-8">
<title>Q7R Services – Business Card</title>
<link href="https://fonts.googleapis.com/css2?family=Lato:ital,wght@0,400;0,700;1,700&display=swap" rel="stylesheet">
<style>
  :root {
    --backdrop: #e4e4e4;
    --paper: #ffffff;
    --ink: #4a4a4a;
    --ink-soft: #5a5a5a;
    --brand-red: #d9232e;
    --rule: #e2e2e2;
    --night: #141414;
    --night-glow: #2e2e2e;
    --band-grey: #5b5b5b;
    --logo-grey: #555555;
  }
  * { box-sizing: border-box; margin: 0; padding: 0; }
  html, body {
    width: 1200px; height: 801px; overflow: hidden;
    background: var(--backdrop);
    font-family: "Lato", Arial, sans-serif;
  }
  .canvas { position: relative; width: 1200px; height: 801px; }

  .card { position: absolute; overflow: hidden; }

  /* Front */
  .card-front {
    left: 355px; top: 40px; width: 515px; height: 313px;
    background: var(--paper);
  }
  .front-brand {
    position: absolute; left: 0; top: 0; width: 265px; height: 276px;
    display: flex; align-items: center; justify-content: center; gap: 8px;
  }
  .brand-mark {
    width: 22px; height: 22px; background: var(--brand-red);
  }
  .brand-name {
    font-weight: 700; font-size: 24px; color: var(--ink);
    letter-spacing: 0.5px;
  }
  .front-divider {
    position: absolute; left: 265px; top: 34px; width: 1px; height: 236px;
    background: var(--rule);
  }
  .person {
    position: absolute; left: 295px; top: 82px;
  }
  .person-name {
    font-size: 24px; font-weight: 400; color: var(--ink); letter-spacing: 0.3px;
    line-height: 1.1;
  }
  .person-role {
    font-size: 13.5px; font-weight: 700; font-style: italic; color: var(--brand-red);
    margin-top: 2px;
  }
  .contact-list {
    position: absolute; left: 295px; top: 147px; list-style: none;
  }
  .contact-item {
    display: flex; align-items: center; gap: 7px;
    height: 25.5px; font-size: 14.5px; color: var(--ink-soft);
  }
  .contact-icon {
    width: 21px; height: 21px; background: var(--brand-red);
    display: flex; align-items: center; justify-content: center; flex: none;
  }
  .service-band {
    position: absolute; left: 0; bottom: 0; width: 100%; height: 37px;
    background: var(--brand-red); color: #fff;
    display: flex; align-items: center; justify-content: center;
    font-size: 13px; font-weight: 700; letter-spacing: 1.1px;
  }
  .service-band .sep { margin: 0 9px; }

  /* Back */
  .card-back {
    left: 353px; top: 419px; width: 518px; height: 314px;
    background: radial-gradient(ellipse at 50% 42%, var(--night-glow) 0%, var(--night) 70%);
  }
  .back-brand {
    position: absolute; left: 0; top: 0; width: 100%; height: 268px;
    display: flex; align-items: center; justify-content: center; gap: 12px;
  }
  .back-brand .brand-mark { width: 30px; height: 30px; }
  .back-brand .brand-name { font-size: 34px; color: var(--logo-grey); letter-spacing: 1px; }
  .motto-band {
    position: absolute; left: 0; top: 268px; width: 100%; height: 27px;
    background: var(--band-grey); color: #fff;
    display: flex; align-items: center; justify-content: center;
    font-size: 14.5px; font-weight: 700; letter-spacing: 2.2px;
  }
</style>
</head>
<body>
<main class="canvas">

  <section class="card card-front" aria-label="Business card front">
    <div class="front-brand">
      <span class="brand-mark"></span>
      <span class="brand-name">Q7R Services</span>
    </div>
    <div class="front-divider"></div>

    <div class="person">
      <p class="person-name">ALEX MORGAN</p>
      <p class="person-role">Managing Director</p>
    </div>

    <ul class="contact-list">
      <li class="contact-item">
        <span class="contact-icon">
          <svg width="13" height="13" viewBox="0 0 24 24" aria-hidden="true"><path fill="#fff" d="M6.6 10.8a15.1 15.1 0 0 0 6.6 6.6l2.2-2.2c.3-.3.7-.4 1-.2 1.1.4 2.3.6 3.6.6.6 0 1 .4 1 1V20c0 .6-.4 1-1 1A17 17 0 0 1 3 4c0-.6.4-1 1-1h3.5c.6 0 1 .4 1 1 0 1.3.2 2.5.6 3.6.1.3 0 .7-.2 1z"/></svg>
        </span>
        (+61) 400512836
      </li>
      <li class="contact-item">
        <span class="contact-icon">
          <svg width="14" height="12" viewBox="0 0 24 18" aria-hidden="true"><rect x="1.5" y="1.5" width="21" height="15" fill="none" stroke="#fff" stroke-width="2"/><path d="M2 2l10 8 10-8" fill="none" stroke="#fff" stroke-width="2"/></svg>
        </span>
        info@Q7RServices.example
      </li>
      <li class="contact-item">
        <span class="contact-icon">
          <svg width="14" height="14" viewBox="0 0 24 24" aria-hidden="true"><g fill="none" stroke="#fff" stroke-width="2"><circle cx="12" cy="12" r="9.5"/><ellipse cx="12" cy="12" rx="4" ry="9.5"/><path d="M2.5 12h19"/></g></svg>
        </span>
        www.Q7RServices.example
      </li>
    </ul>

    <div class="service-band">
      ELECTRICAL<span class="sep">|</span>HYDRAULIC<span class="sep">|</span>MECHANICAL<span class="sep">|</span>CIVIL SERVICES
    </div>
  </section>

  <section class="card card-back" aria-label="Business card back">
    <div class="back-brand">
      <span class="brand-mark"></span>
      <span class="brand-name">Q7R Services</span>
    </div>
    <div class="motto-band">DESIGN - DOCUMENT - DEVELOP - DELIVER</div>
  </section>

</main>
</body>
</html>
```